Quillo App - Live Events Stream

Need mobile first appliation designs for a new location based events and offers application <br/><br/>Will require at least 5 screens creating, namely:<br/><br/>- Landing screen<br/>- Event/Offer listings screen<br/>- Overview of Event/Offer screen<br/>- Chat/Stream for Event/Offer<br/>- Directions for Event/Offer<br/>- Create Event/Offer screen(s)<br/><br/>Will require the design to have a google material feel. <br/><br/>See Attached files for further details

Requirements
Must have
• See Doc
Nice to have
• See Doc
Should not have
• See Doc

```html
<!DOCTYPE html>
<html lang="en">
<head>
<meta charset="utf-8">
<title>Quillo App – Live Events Stream</title>
<link rel="stylesheet" href="https://fonts.googleapis.com/css2?family=Roboto:wght@400;500&display=swap">
<style>
  :root {
    --bg: #f0f4f0;
    --screen: #ffffff;
    --pink: #e8a6e2;
    --teal: #8cdce0;
    --teal-text: #5fcdd4;
    --yellow: #ecd96c;
    --ink: #1d1f24;
    --muted: #a9acb2;
    --map: #eeeeee;
    --map-road: #f9f9f9;
    --blue: #2aa9ea;
    --blue-halo: rgba(120, 200, 240, 0.55);
    --divider: #e4e6ea;
  }
  * { box-sizing: border-box; margin: 0; padding: 0; }
  html, body { width: 1200px; height: 1090px; overflow: hidden; }
  body { background: var(--bg); font-family: "Roboto", Arial, sans-serif; color: var(--ink); position: relative; }

  .screen { position: absolute; width: 320px; height: 692px; background: var(--screen); border-radius: 26px; overflow: hidden; box-shadow: 0 10px 30px rgba(0,0,0,.08); }
  .screen--map { left: 223px; top: 205px; }
  .screen--list { left: 675px; top: 270px; }

  .topbar { position: absolute; left: 0; right: 0; top: 56px; height: 28px; display: flex; align-items: center; justify-content: center; }
  .topbar__title { font-size: 14px; font-weight: 400; color: var(--pink); }
  .screen--list .topbar__title { color: #fff; font-size: 14px; }
  .topbar__menu { position: absolute; left: 24px; top: 7px; }
  .topbar__actions { position: absolute; right: 24px; top: 6px; display: flex; gap: 10px; }

  .search { position: absolute; left: 25px; width: 270px; top: 98px; height: 31px; background: #fff; border-radius: 16px; box-shadow: 0 2px 8px rgba(0,0,0,.08); display: flex; align-items: center; padding: 0 16px; font-size: 8px; color: var(--muted); justify-content: space-between; z-index: 2; }

  .map { position: absolute; left: 0; right: 0; top: 112px; height: 380px; background: linear-gradient(160deg, #efefef, #e8e8e8 60%, #f2f2f2); }
  .map__pin { position: absolute; width: 22px; height: 22px; border-radius: 50%; border: 4px solid #fff; box-shadow: 0 1px 4px rgba(0,0,0,.12); }
  .map__pin--pink { background: var(--pink); }
  .map__pin--yellow { background: var(--yellow); }
  .map__halo { position: absolute; width: 58px; height: 58px; border-radius: 50%; background: var(--blue-halo); }
  .map__me { position: absolute; width: 12px; height: 12px; border-radius: 50%; background: var(--blue); border: 2px solid #fff; }

  .mini-card { position: absolute; top: 489px; width: 183px; height: 148px; background: #fff; border-radius: 6px; overflow: hidden; box-shadow: 0 2px 10px rgba(0,0,0,.08); }
  .mini-card__photo { height: 104px; background: linear-gradient(180deg, #5a3ea6 0%, #3b2a70 45%, #1c1a2c 100%); position: relative; }
  .mini-card__name, .event__name { position: absolute; left: 13px; bottom: 13px; color: #fff; font-size: 10.5px; font-weight: 500; white-space: nowrap; }
  .meta { display: flex; align-items: center; gap: 5px; font-size: 6.2px; color: var(--ink); }
  .mini-card__meta { padding: 10px 13px 0; display: flex; flex-direction: column; gap: 6px; }

  .list-head { position: absolute; left: 0; right: 0; top: 0; height: 112px; background: var(--teal); }

  .event { position: absolute; left: 24px; width: 271px; background: #fff; border-radius: 6px; overflow: hidden; box-shadow: 0 2px 10px rgba(0,0,0,.08); }
  .event__photo { height: 145px; position: relative; }
  .event__photo--purple { background: linear-gradient(180deg, #4d3796 0%, #3b2e74 50%, #1e1b30 100%); }
  .event__photo--blue { background: linear-gradient(160deg, #3f6fae 0%, #2a5486 45%, #1d2f4f 100%); }
  .event__photo--stage { background: linear-gradient(180deg, #6b7fc4 0%, #8b6c9a 55%, #c46a36 100%); }
  .event__badge { position: absolute; left: 0; top: 12px; padding: 3px 11px; font-size: 7px; color: #fff; }
  .badge--now { background: var(--teal); }
  .badge--later { background: var(--pink); }
  .badge--soon { background: var(--yellow); }
  .event__info { display: flex; justify-content: space-between; padding: 8px 14px 0; }
  .event__when { display: flex; flex-direction: column; gap: 6px; }
  .event__where { display: flex; gap: 5px; font-size: 6px; line-height: 1.35; width: 118px; }
  .event__actions { margin: 9px 14px 0; border-top: 1px solid var(--divider); display: flex; align-items: center; height: 27px; font-size: 6.5px; font-weight: 500; letter-spacing: .2px; }
  .event__action { flex: 1; display: flex; align-items: center; justify-content: center; gap: 5px; }
  .event__action--msg { color: var(--teal-text); }
  .event__action--views { color: var(--pink); }
  .event__sep { width: 1px; height: 8px; background: var(--divider); }
</style>
</head>
<body>

<!-- Nearest events map screen -->
<section class="screen screen--map">
  <div class="map" role="img" aria-label="Street map of the surrounding city area with event locations">
    <span class="map__pin map__pin--pink" style="left:73px;top:36px"></span>
    <span class="map__pin map__pin--pink" style="left:173px;top:60px"></span>
    <span class="map__pin map__pin--pink" style="left:52px;top:138px"></span>
    <span class="map__pin map__pin--pink" style="left:248px;top:138px"></span>
    <span class="map__pin map__pin--yellow" style="left:150px;top:157px"></span>
    <span class="map__pin map__pin--pink" style="left:32px;top:252px"></span>
    <span class="map__pin map__pin--yellow" style="left:224px;top:257px"></span>
    <span class="map__pin map__pin--yellow" style="left:115px;top:280px"></span>
    <span class="map__halo" style="left:145px;top:207px"></span>
    <span class="map__me" style="left:167px;top:229px"></span>
  </div>

  <header class="topbar">
    <svg class="topbar__menu" width="14" height="12" viewBox="0 0 14 12"><rect y="0" width="14" height="2" fill="#1d1f24"/><rect y="5" width="14" height="2" fill="#1d1f24"/><rect y="10" width="14" height="2" fill="#1d1f24"/></svg>
    <h1 class="topbar__title">Nearest Events</h1>
    <div class="topbar__actions">
      <svg width="12" height="12" viewBox="0 0 12 12"><path d="M0 0h12L7.3 5.6V12L4.7 10.5V5.6z" fill="#1d1f24"/></svg>
      <svg width="11" height="12" viewBox="0 0 11 12"><circle cx="5.5" cy="3" r="3" fill="#1d1f24"/><path d="M0 12c0-3.5 2.4-5 5.5-5S11 8.5 11 12z" fill="#1d1f24"/></svg>
    </div>
  </header>

  <div class="search">
    <span>Search Events...</span>
    <svg width="11" height="11" viewBox="0 0 11 11"><circle cx="4.5" cy="4.5" r="3.7" fill="none" stroke="#a9acb2" stroke-width="1.2"/><path d="M7.3 7.3L10.5 10.5" stroke="#a9acb2" stroke-width="1.2"/></svg>
  </div>

  <article class="mini-card" style="left:25px">
    <div class="mini-card__photo" role="img" aria-label="Concert crowd with raised hands under purple stage lights">
      <span class="mini-card__name">Carnival Night Festival</span>
    </div>
    <div class="mini-card__meta">
      <span class="meta"><svg width="7" height="7" viewBox="0 0 7 7"><rect x=".5" y="1" width="6" height="5.5" fill="none" stroke="#1d1f24"/><rect x=".5" y="1" width="6" height="1.6" fill="#1d1f24"/></svg>Tus, 10 Mar 2020</span>
      <span class="meta"><svg width="7" height="7" viewBox="0 0 7 7"><circle cx="3.5" cy="3.5" r="3.2" fill="#1d1f24"/><path d="M3.5 1.6V3.6H5" stroke="#fff" stroke-width=".8" fill="none"/></svg>08:00 PM</span>
    </div>
  </article>
  <article class="mini-card" style="left:220px">
    <div class="mini-card__photo" role="img" aria-label="Concert crowd with raised hands under purple stage lights">
      <span class="mini-card__name">Carnival Night Festival</span>
    </div>
    <div class="mini-card__meta">
      <span class="meta"><svg width="7" height="7" viewBox="0 0 7 7"><rect x=".5" y="1" width="6" height="5.5" fill="none" stroke="#1d1f24"/><rect x=".5" y="1" width="6" height="1.6" fill="#1d1f24"/></svg>Tus, 10 Mar 2020</span>
      <span class="meta"><svg width="7" height="7" viewBox="0 0 7 7"><circle cx="3.5" cy="3.5" r="3.2" fill="#1d1f24"/><path d="M3.5 1.6V3.6H5" stroke="#fff" stroke-width=".8" fill="none"/></svg>08:00 PM</span>
    </div>
  </article>
</section>

<!-- Events list screen -->
<section class="screen screen--list">
  <div class="list-head"></div>
  <header class="topbar" style="top:56px">
    <svg class="topbar__menu" width="14" height="12" viewBox="0 0 14 12"><rect y="0" width="14" height="2" fill="#fff"/><rect y="5" width="14" height="2" fill="#fff"/><rect y="10" width="14" height="2" fill="#fff"/></svg>
    <h1 class="topbar__title">Events List</h1>
    <div class="topbar__actions">
      <svg width="12" height="12" viewBox="0 0 12 12"><path d="M0 0h12L7.3 5.6V12L4.7 10.5V5.6z" fill="#fff"/></svg>
      <svg width="11" height="12" viewBox="0 0 11 12"><circle cx="5.5" cy="3" r="3" fill="#fff"/><path d="M0 12c0-3.5 2.4-5 5.5-5S11 8.5 11 12z" fill="#fff"/></svg>
    </div>
  </header>

  <div class="search" style="left:24px;top:98px">
    <span>Search Events...</span>
    <svg width="11" height="11" viewBox="0 0 11 11"><circle cx="4.5" cy="4.5" r="3.7" fill="none" stroke="#a9acb2" stroke-width="1.2"/><path d="M7.3 7.3L10.5 10.5" stroke="#a9acb2" stroke-width="1.2"/></svg>
  </div>

  <article class="event" style="top:150px">
    <div class="event__photo event__photo--purple" role="img" aria-label="Festival crowd cheering in front of a purple lit stage">
      <span class="event__badge badge--now">Now</span>
      <span class="event__name">Carnival Night Festival</span>
    </div>
    <div class="event__info">
      <div class="event__when">
        <span class="meta"><svg width="7" height="7" viewBox="0 0 7 7"><rect x=".5" y="1" width="6" height="5.5" fill="none" stroke="#1d1f24"/><rect x=".5" y="1" width="6" height="1.6" fill="#1d1f24"/></svg>Tus, 10 Mar 2020</span>
        <span class="meta"><svg width="7" height="7" viewBox="0 0 7 7"><circle cx="3.5" cy="3.5" r="3.2" fill="#1d1f24"/><path d="M3.5 1.6V3.6H5" stroke="#fff" stroke-width=".8" fill="none"/></svg>08:00 PM</span>
      </div>
      <div class="event__where">
        <svg width="6" height="8" viewBox="0 0 6 8"><path d="M3 0a3 3 0 0 1 3 3c0 2-3 5-3 5S0 5 0 3a3 3 0 0 1 3-3z" fill="#1d1f24"/><circle cx="3" cy="3" r="1" fill="#fff"/></svg>
        <span>Maple Lane 2nd Block 4th Cross, Riverside, Lakeview-500210</span>
      </div>
    </div>
    <div class="event__actions">
      <span class="event__action event__action--msg"><svg width="9" height="8" viewBox="0 0 9 8"><path d="M4.5 0C7 0 9 1.5 9 3.4S7 6.8 4.5 6.8c-.6 0-1.1 0-1.6-.2L.6 8l.7-2C.5 5.3 0 4.4 0 3.4 0 1.5 2 0 4.5 0z" fill="#8cdce0"/></svg>SEND MESSAGE</span>
      <span class="event__sep"></span>
      <span class="event__action event__action--views"><svg width="9" height="6" viewBox="0 0 9 6"><path d="M0 3c1.3-2 2.8-3 4.5-3S7.7 1 9 3C7.7 5 6.2 6 4.5 6S1.3 5 0 3z" fill="#e8a6e2"/><circle cx="4.5" cy="3" r="1.3" fill="#fff"/></svg>12K VIEWS</span>
    </div>
  </article>

  <article class="event" style="top:379px">
    <div class="event__photo event__photo--blue" role="img" aria-label="Two fans dancing with raised arms at a concert">
      <span class="event__badge badge--later">Later</span>
      <span class="event__name">Carnival Night Festival</span>
    </div>
    <div class="event__info">
      <div class="event__when">
        <span class="meta"><svg width="7" height="7" viewBox="0 0 7 7"><rect x=".5" y="1" width="6" height="5.5" fill="none" stroke="#1d1f24"/><rect x=".5" y="1" width="6" height="1.6" fill="#1d1f24"/></svg>Tus, 10 Mar 2020</span>
        <span class="meta"><svg width="7" height="7" viewBox="0 0 7 7"><circle cx="3.5" cy="3.5" r="3.2" fill="#1d1f24"/><path d="M3.5 1.6V3.6H5" stroke="#fff" stroke-width=".8" fill="none"/></svg>08:00 PM</span>
      </div>
      <div class="event__where">
        <svg width="6" height="8" viewBox="0 0 6 8"><path d="M3 0a3 3 0 0 1 3 3c0 2-3 5-3 5S0 5 0 3a3 3 0 0 1 3-3z" fill="#1d1f24"/><circle cx="3" cy="3" r="1" fill="#fff"/></svg>
        <span>Maple Lane 2nd Block 4th Cross, Riverside, Lakeview-500210</span>
      </div>
    </div>
    <div class="event__actions">
      <span class="event__action event__action--msg"><svg width="9" height="8" viewBox="0 0 9 8"><path d="M4.5 0C7 0 9 1.5 9 3.4S7 6.8 4.5 6.8c-.6 0-1.1 0-1.6-.2L.6 8l.7-2C.5 5.3 0 4.4 0 3.4 0 1.5 2 0 4.5 0z" fill="#8cdce0"/></svg>SEND MESSAGE</span>
      <span class="event__sep"></span>
      <span class="event__action event__action--views"><svg width="9" height="6" viewBox="0 0 9 6"><path d="M0 3c1.3-2 2.8-3 4.5-3S7.7 1 9 3C7.7 5 6.2 6 4.5 6S1.3 5 0 3z" fill="#e8a6e2"/><circle cx="4.5" cy="3" r="1.3" fill="#fff"/></svg>12K VIEWS</span>
    </div>
  </article>

  <article class="event" style="top:609px">
    <div class="event__photo event__photo--stage" role="img" aria-label="Band on stage in front of a crowd lit in orange">
      <span class="event__badge badge--soon">Soon</span>
    </div>
  </article>
</section>

</body>
</html>
```